Personal Chef Business Card Design

My company, Simmerly, is a personal in-home chef service that caters to clients' needs, but I am not a caterer. The types of services that I provide range from : weekly menus for busy families, special menus for specific diets, custom menus, private parties, intimate dinners, and brunch parties. My cooking style is seasonal and simple with the option of a variety of cuisines. I like colorful and simple business cards. My business is just getting started as I will be the only employee for now. I would like to be able to use the design on the card for my logo also. I don't know if logo design is a different service altogether.

If you can convince me to go with double-sided, then so be it, but until then, I'll stick with singe-sided.

Target Market(s)

busy families, health conscious, private parties, brunch parties, dinner parties

Industry/Entity Type

Chef

Contact Information for Business Card

Ross Tamblyn
rosstamblyn@mailvora.com
434-817-2290
Simmerly Personal Chef Service
Serving the DC/VA/MD area

Font styles to use
Serif
Sans Serif
Decorative
Script
Other font styles liked:
• Anything

Requirements
Must have
• I will be using the illustration as my logo so that I can use it for promotional merchandise.

```html
<!DOCTYPE html>
<html lang="en">
<head>
<meta charset="utf-8">
<title>Simmerly Personal Chef Service – Business Card</title>
<link rel="stylesheet" href="https://fonts.googleapis.com/css2?family=Amatic+SC:wght@400&family=Quicksand:wght@400;500&display=swap">
<style>
  :root {
    --backdrop: #ece8e2;
    --card: #ffffff;
    --orange: #e8973a;
    --orange-text: #e8842c;
    --grey-text: #8a8a8a;
    --icon-grey: #9a9a9a;
    --on-orange: #ffffff;
  }
  * { margin: 0; padding: 0; box-sizing: border-box; }
  html, body {
    width: 1200px;
    height: 800px;
    overflow: hidden;
    background: var(--backdrop);
  }
  .canvas {
    position: relative;
    width: 1200px;
    height: 800px;
    display: flex;
    align-items: center;
    justify-content: center;
  }
  .business-card {
    position: relative;
    width: 900px;
    height: 514px;
    background: var(--card);
    box-shadow: 0 6px 24px rgba(0,0,0,0.12);
  }
  .brand-seal {
    position: absolute;
    left: 60px;
    top: 87px;
    width: 340px;
    height: 340px;
    border-radius: 50%;
    background: var(--orange);
    display: flex;
    flex-direction: column;
    align-items: center;
    justify-content: center;
    color: var(--on-orange);
    font-family: "Quicksand", sans-serif;
    font-weight: 500;
    text-align: center;
  }
  .brand-name {
    font-size: 52px;
    line-height: 1;
    letter-spacing: 1px;
    text-transform: uppercase;
  }
  .brand-tagline {
    margin-top: 6px;
    font-size: 20px;
    line-height: 1.2;
  }
  .contact-block {
    position: absolute;
    left: 470px;
    top: 150px;
  }
  .person-name {
    font-family: "Amatic SC", cursive;
    font-weight: 400;
    font-size: 92px;
    line-height: 1;
    letter-spacing: 10px;
    color: var(--orange-text);
    text-transform: uppercase;
    margin-bottom: 18px;
  }
  .contact-list {
    list-style: none;
    font-family: "Quicksand", sans-serif;
    font-weight: 400;
    font-size: 24px;
    color: var(--grey-text);
  }
  .contact-item {
    display: flex;
    align-items: center;
    gap: 14px;
    height: 44px;
  }
  .contact-icon {
    width: 26px;
    height: 26px;
    flex-shrink: 0;
  }
</style>
</head>
<body>
<main class="canvas">
  <section class="business-card">
    <div class="brand-seal">
      <span class="brand-name">Simmerly</span>
      <span class="brand-tagline">Personal Chef Service</span>
    </div>

    <div class="contact-block">
      <h1 class="person-name">Ross Tamblyn</h1>
      <ul class="contact-list">
        <li class="contact-item">
          <svg class="contact-icon" viewBox="0 0 26 26" aria-hidden="true">
            <circle cx="13" cy="13" r="11.5" fill="none" stroke="var(--icon-grey)" stroke-width="2"/>
            <path d="M9 7.5c.6-.4 1.3-.3 1.7.3l1 1.6c.3.5.2 1.1-.2 1.5l-.7.6c.6 1.4 1.7 2.5 3.1 3.1l.6-.7c.4-.4 1-.5 1.5-.2l1.6 1c.6.4.7 1.1.3 1.7l-.6.8c-.6.7-1.6 1-2.5.6-3.1-1.3-5.5-3.7-6.8-6.8-.4-.9-.1-1.9.6-2.5z" fill="var(--icon-grey)"/>
          </svg>
          <span>434-817-2290</span>
        </li>
        <li class="contact-item">
          <svg class="contact-icon" viewBox="0 0 26 26" aria-hidden="true">
            <circle cx="13" cy="13" r="12.5" fill="var(--icon-grey)"/>
            <rect x="6.5" y="8.5" width="13" height="9" rx="1" fill="none" stroke="#fff" stroke-width="1.6"/>
            <path d="M7 9l6 5 6-5" fill="none" stroke="#fff" stroke-width="1.6"/>
          </svg>
          <span>rosstamblyn@mailvora.com</span>
        </li>
        <li class="contact-item">
          <svg class="contact-icon" viewBox="0 0 26 26" aria-hidden="true">
            <path d="M13 2.5c-4.1 0-7.3 3.2-7.3 7.2 0 5.4 7.3 13.8 7.3 13.8s7.3-8.4 7.3-13.8c0-4-3.2-7.2-7.3-7.2z" fill="var(--icon-grey)"/>
            <circle cx="13" cy="9.8" r="2.8" fill="#fff"/>
          </svg>
          <span>Serving the DC/VA/MD area</span>
        </li>
      </ul>
    </div>
  </section>
</main>
</body>
</html>
```